Forensic Psychology and Polygraph Needs Clever Catchy Logo

There's a massive trade show coming up and we are looking to debut a new, clever logo for our business cards. We are a private practice that offers psychological evaluations, therapeutic counseling, and polygraphing. Our website is ketvorin.com (to get a better idea of the color scheme) and instead of the nature/cuddly image that other psychology organizations like to go for, we are interested in cultivating a business, strength, and professional image.
Attached are some popular logos and designs to get those creative juices flowing! I would like to avoid the brain/psi logo as this has been to death so bonus points definitely for originality.
Target Market(s)
governmental agencies, third party mental health providers, individual private pay clients
Industry/Entity Type
Mental Health
Contact Information for Business Card
One one side will be the logo and company name while on the back will be contact information and provider details (name, position, etc)
Look and feel

```html
<!DOCTYPE html>
<html lang="en">
<head>
<meta charset="utf-8">
<title>Marlowe &amp; Associates – Business Card</title>
<link rel="stylesheet" href="https://fonts.googleapis.com/css2?family=Source+Sans+3:wght@400;600&display=swap">
<style>
  :root {
    --teal: #1bb0aa;
    --ink: #1c2a33;
    --paper: #ffffff;
    --backdrop: #c9cbcc;
  }
  * { box-sizing: border-box; margin: 0; padding: 0; }
  html, body { width: 1200px; height: 808px; overflow: hidden; }
  body {
    background: var(--backdrop);
    font-family: "Source Sans 3", Arial, sans-serif;
    position: relative;
  }
  .card {
    position: absolute;
    width: 540px;
    height: 309px;
    background: var(--paper);
    overflow: hidden;
    box-shadow: 0 6px 18px rgba(0,0,0,0.18);
  }
  .card-front { left: 40px; top: 250px; }
  .card-back { left: 620px; top: 250px; }
  .card-shape { position: absolute; inset: 0; width: 100%; height: 100%; }

  .brand {
    position: absolute;
    left: 60px;
    top: 118px;
    display: flex;
    align-items: center;
    gap: 18px;
  }
  .brand-dot {
    width: 54px; height: 54px;
    border-radius: 50%;
    background: var(--paper);
    flex: none;
  }
  .brand-name {
    color: var(--ink);
    font-weight: 400;
    font-size: 34px;
    line-height: 1;
    letter-spacing: 0.5px;
    text-transform: uppercase;
  }
  .brand-tagline {
    position: absolute;
    left: 132px;
    top: 166px;
    color: var(--paper);
    font-size: 19px;
    font-weight: 400;
  }

  .contact-list {
    position: absolute;
    left: 34px;
    top: 168px;
    list-style: none;
  }
  .contact-item {
    display: flex;
    align-items: center;
    gap: 14px;
    color: var(--teal);
    font-size: 14.5px;
    line-height: 1.15;
    height: 30px;
  }
  .contact-icon { width: 22px; height: 22px; flex: none; }
  .contact-item.address { height: 40px; }
</style>
</head>
<body>

  <section class="card card-front">
    <svg class="card-shape" viewBox="0 0 540 309" aria-hidden="true">
      <path d="M0 70 Q 250 95 430 0 L540 0 L540 309 L0 309 Z" fill="var(--teal)"/>
    </svg>
    <div class="brand">
      <span class="brand-dot"></span>
      <span class="brand-name">Marlowe &amp; Associates</span>
    </div>
    <p class="brand-tagline">Psychological Services, PLLC</p>
  </section>

  <section class="card card-back">
    <svg class="card-shape" viewBox="0 0 540 309" aria-hidden="true">
      <path d="M0 0 H540 V70 Q 470 95 300 105 Q 140 118 0 170 Z" fill="var(--teal)"/>
    </svg>
    <ul class="contact-list">
      <li class="contact-item">
        <svg class="contact-icon" viewBox="0 0 24 24" aria-hidden="true">
          <path d="M3 9c0-3 4-5 9-5s9 2 9 5l-3 1-2-3H8L6 10z" fill="var(--teal)"/>
          <rect x="5" y="11" width="14" height="9" rx="2" fill="var(--teal)"/>
          <circle cx="12" cy="15.5" r="2.5" fill="var(--paper)"/>
        </svg>
        <span>602.555.0148</span>
      </li>
      <li class="contact-item">
        <svg class="contact-icon" viewBox="0 0 24 24" aria-hidden="true">
          <rect x="2" y="5" width="20" height="14" fill="none" stroke="var(--teal)" stroke-width="2"/>
          <path d="M2 5l10 8 10-8" fill="none" stroke="var(--teal)" stroke-width="2"/>
        </svg>
        <span>contact@ketvorin.com</span>
      </li>
      <li class="contact-item">
        <svg class="contact-icon" viewBox="0 0 24 24" aria-hidden="true">
          <circle cx="12" cy="12" r="9.5" fill="none" stroke="var(--teal)" stroke-width="2"/>
          <ellipse cx="12" cy="12" rx="4" ry="9.5" fill="none" stroke="var(--teal)" stroke-width="1.6"/>
          <path d="M2.5 12h19M4 7h16M4 17h16" stroke="var(--teal)" stroke-width="1.6"/>
        </svg>
        <span>www.ketvorin.com</span>
      </li>
      <li class="contact-item address">
        <svg class="contact-icon" viewBox="0 0 24 24" aria-hidden="true">
          <path d="M12 2a7 7 0 0 0-7 7c0 5 7 13 7 13s7-8 7-13a7 7 0 0 0-7-7z" fill="var(--teal)"/>
          <circle cx="12" cy="9" r="2.6" fill="var(--paper)"/>
        </svg>
        <span>4872 N. Larkmoor Ave, Floor 3, Office 12<br>Brenholt, Arizona 85999</span>
      </li>
    </ul>
  </section>

</body>
</html>
```